Graphic Design Needed for Powerpoint Deck

We need a powerpoint design template, font, and look and feel for a new company called Meadow Wellness. Specific needs are listed in the attached file and if we like what we see we will more than likely use you in the future.
We like warm natural colors from a branding point of view, greens, browns, etc.
Target Market(s)
This will be used with potential investors and business partners.
Industry/Entity Type
Graphic Design
Requirements
Must have
- Graphic Designs for the charts mentioned in the powerpoint
- Overall Look and Feel
Nice to have
- Custom Font recommendations (Trebuchet is the one we like the most that is standard)

```html
<!DOCTYPE html>
<html lang="en">
<head>
<meta charset="utf-8">
<title>Meadow Wellness – Pricing Plans</title>
<link rel="stylesheet" href="https://fonts.googleapis.com/css2?family=Oswald:wght@400;500;600&family=PT+Sans:wght@400;700&display=swap">
<style>
  :root {
    --bar-dark: #3d3d3d;
    --paper: #ebe8e2;
    --band: #f1f1f1;
    --ink: #1e1e1e;
    --white: #ffffff;
    --silver: #d4d4d4;
    --gold-top: #f3bb05;
    --gold-bottom: #c79800;
    --platinum: #fdfdfd;
    --platinum-dot: #d9d9d9;
    --executive: #df7420;
  }
  * { box-sizing: border-box; margin: 0; padding: 0; }
  html, body { width: 1200px; height: 900px; overflow: hidden; }
  body {
    position: relative;
    background: var(--paper);
    font-family: "PT Sans", "Trebuchet MS", sans-serif;
    color: var(--ink);
  }
  .slide-header {
    position: absolute; left: 0; top: 0; width: 1200px; height: 103px;
    background: var(--bar-dark);
  }
  .slide-title {
    position: absolute; left: 27px; top: 24px;
    font-family: "Oswald", sans-serif; font-weight: 500;
    font-size: 43px; line-height: 52px; letter-spacing: 0.5px;
    color: var(--white); text-transform: uppercase;
  }
  .plan-card {
    position: absolute; top: 200px; width: 197px; height: 333px;
    border-radius: 10px;
  }
  .plan-card--silver { left: 150px; background: var(--silver); }
  .plan-card--gold { left: 400px; background: linear-gradient(var(--gold-top), var(--gold-bottom)); }
  .plan-card--platinum { left: 667px; background: var(--platinum); }
  .plan-card--executive { left: 885px; background: var(--executive); }
  .plan-badge {
    position: absolute; left: 50%; top: 147px;
    width: 110px; height: 110px; margin: -55px 0 0 -55px;
    border-radius: 50%; background: var(--white);
    display: flex; align-items: center; justify-content: center;
    font-family: "Oswald", sans-serif; font-weight: 500; font-size: 23px;
    text-transform: uppercase; color: var(--ink);
  }
  .plan-card--gold .plan-badge { width: 126px; height: 126px; margin: -63px 0 0 -63px; }
  .plan-card--platinum .plan-badge { background: var(--platinum-dot); }
  .plan-card--executive .plan-badge { width: 116px; height: 116px; margin: -58px 0 0 -58px; }
  .plan-audience {
    position: absolute; left: 0; right: 0; top: 246px; text-align: center;
    font-family: "Oswald", sans-serif; font-size: 16px; text-transform: uppercase;
  }
  .plan-price {
    position: absolute; left: 0; right: 0; top: 280px; text-align: center;
    font-family: "Oswald", sans-serif; font-weight: 500; font-size: 22px;
  }
  .plan-card--silver .plan-price { top: 276px; }
  .services-band {
    position: absolute; left: 0; top: 708px; width: 1200px; height: 192px;
    background: var(--band);
  }
  .services-heading {
    position: absolute; left: 23px; top: 664px;
    font-family: "Oswald", sans-serif; font-weight: 500; font-size: 27px;
    text-transform: uppercase; border-bottom: 2px solid var(--ink); line-height: 36px;
  }
  .service { position: absolute; top: 755px; text-align: center; }
  .service-name {
    display: block; height: 42px; line-height: 42px;
    background: var(--bar-dark); color: var(--white); font-size: 26px;
    white-space: nowrap;
  }
  .service-price {
    display: block; margin-top: 16px; font-size: 26px; white-space: nowrap;
  }
</style>
</head>
<body>
  <header class="slide-header">
    <h1 class="slide-title">Pricing Plans</h1>
  </header>

  <section class="plans">
    <article class="plan-card plan-card--silver">
      <div class="plan-badge">Silver</div>
      <p class="plan-audience">Individual &amp; Family</p>
      <p class="plan-price">$1,800-$6,000</p>
    </article>
    <article class="plan-card plan-card--gold">
      <div class="plan-badge">Gold</div>
      <p class="plan-price">$2,400</p>
    </article>
    <article class="plan-card plan-card--platinum">
      <div class="plan-badge">Platinum</div>
      <p class="plan-price">$7,800</p>
    </article>
    <article class="plan-card plan-card--executive">
      <div class="plan-badge">Executive</div>
      <p class="plan-price">14,400</p>
    </article>
  </section>

  <div class="services-band"></div>
  <h2 class="services-heading">Al a Cart Services</h2>

  <section class="services">
    <div class="service" style="left:20px;width:170px"><span class="service-name">Chiropractor</span><span class="service-price">$60 - $2,500</span></div>
    <div class="service" style="left:235px;width:197px"><span class="service-name">Fitness Center</span><span class="service-price">$1,200/ year</span></div>
    <div class="service" style="left:463px;width:158px"><span class="service-name">Nutritionist</span><span class="service-price">$500</span></div>
    <div class="service" style="left:665px;width:108px"><span class="service-name">Massage</span><span class="service-price">$120</span></div>
    <div class="service" style="left:838px;width:107px"><span class="service-name">Classes</span><span class="service-price">$60</span></div>
    <div class="service" style="left:995px;width:173px"><span class="service-name">Supplements</span><span class="service-price">$360/ year</span></div>
  </section>
</body>
</html>
```